Tolvane Clinica Business Card Design and print

I have attached the design I require including JPEG for company logo. I would like a copy of the art work for future needs.

Double sided - the item will not change from single

250 cards with both names on Ruth Pellow and Carol Dunmore

250 cards with Ruth Pellow only

Industry/Entity Type

Business

Contact Information for Business Card

See attached layout

```html
<!DOCTYPE html>
<html lang="en">
<head>
<meta charset="utf-8">
<title>Tolvane Clinica – Business Card</title>
<link rel="stylesheet" href="https://fonts.googleapis.com/css2?family=Lato:wght@300;400;700&display=swap">
<style>
  :root {
    --purple: #814c9f;
    --orange: #dd7324;
    --white: #ffffff;
    --ink: #1c1c1c;
    --backdrop: #e8e8ea;
  }
  * { margin: 0; padding: 0; box-sizing: border-box; }
  html, body {
    width: 1200px;
    height: 800px;
    overflow: hidden;
    background: var(--backdrop);
    font-family: "Lato", Arial, sans-serif;
  }
  .stage {
    position: relative;
    width: 1200px;
    height: 800px;
  }
  .card {
    position: absolute;
    top: 252px;
    width: 520px;
    height: 297px;
    overflow: hidden;
    box-shadow: 0 6px 18px rgba(0,0,0,0.12);
  }

  /* Front side */
  .card-front {
    left: 50px;
    background: var(--purple);
    color: var(--white);
    display: flex;
    flex-direction: column;
    align-items: center;
    justify-content: center;
  }
  .brand-line {
    display: flex;
    align-items: center;
    gap: 12px;
    font-weight: 300;
    font-size: 34px;
    letter-spacing: 0.5px;
    text-transform: lowercase;
  }
  .brand-square {
    width: 34px;
    height: 34px;
    background: var(--white);
  }
  .front-web {
    margin-top: 22px;
    font-size: 13px;
    font-weight: 400;
    letter-spacing: 0.3px;
  }

  /* Back side */
  .card-back {
    left: 630px;
    background: var(--white);
  }
  .contacts {
    position: absolute;
    left: 70px;
    top: 38px;
    color: var(--ink);
  }
  .person + .person { margin-top: 14px; }
  .person-name {
    font-weight: 700;
    font-size: 15px;
    margin-bottom: 2px;
  }
  .person-detail {
    font-size: 12px;
    line-height: 1.4;
  }
  .bands {
    position: absolute;
    left: 0;
    bottom: 0;
    width: 520px;
    height: 80px;
  }
  .back-web {
    position: absolute;
    left: 22px;
    bottom: 38px;
    color: var(--white);
    font-size: 12px;
    letter-spacing: 0.3px;
  }
  .back-brand {
    position: absolute;
    right: 36px;
    bottom: 72px;
    display: flex;
    align-items: center;
    gap: 10px;
    color: var(--orange);
    font-weight: 300;
    font-size: 28px;
  }
  .back-brand .brand-square {
    width: 28px;
    height: 28px;
    background: var(--purple);
  }
</style>
</head>
<body>
<main class="stage">

  <section class="card card-front" aria-label="Card front">
    <div class="brand-line">
      <span>tolvane clinica</span>
      <span class="brand-square"></span>
    </div>
    <p class="front-web">www.tolvaneclinica.com.au</p>
  </section>

  <section class="card card-back" aria-label="Card back">
    <div class="contacts">
      <div class="person">
        <p class="person-name">Ruth Pellow</p>
        <p class="person-detail">ruth@tolvaneclinica.com.au</p>
        <p class="person-detail">+61 (0)400 555 018</p>
      </div>
      <div class="person">
        <p class="person-name">Carol Dunmore</p>
        <p class="person-detail">carol@tolvaneclinica.com.au</p>
        <p class="person-detail">+61 (0)400 555 027</p>
      </div>
    </div>

    <svg class="bands" viewBox="0 0 520 80" aria-hidden="true">
      <polygon points="0,12 228,12 238,56 0,56" fill="var(--orange)"/>
      <rect x="0" y="56" width="520" height="24" fill="var(--purple)"/>
    </svg>
    <p class="back-web">www.tolvaneclinica.com.au</p>

    <div class="back-brand">
      <span>Tolvane Clinica</span>
      <span class="brand-square"></span>
    </div>
  </section>

</main>
</body>
</html>
```